New National Dermatology Group needs a business card!

We need a business card for our new national company that has 3 brands within the business:
Brellow Clinics Australia, Tamvirk Clinics Australia and Orvandel Clinics Australia.
We help people access dermatology services close to home throughout Australia.
We need a business card that has:
all 3 logos on it,
Our websites (there are three, listed above)
Our email (there are three, listed above)
The location of our first clinic: 41 Wendle St Parramatta (this can then be changed for each location as required)

```html
<!DOCTYPE html>
<html lang="en">
<head>
<meta charset="utf-8">
<title>Business Card – National Dermatology Group</title>
<link rel="stylesheet" href="https://fonts.googleapis.com/css2?family=Lato:wght@400;700&display=swap">
<style>
  :root {
    --backdrop: #1e9a42;
    --card: #f4f4f3;
    --charcoal: #2a2a2a;
    --green: #1fa447;
    --brown: #7a3a12;
    --orange: #e0792a;
    --ink: #1f1f1f;
    --light-text: #e8e8e8;
    --white: #ffffff;
  }
  * { margin: 0; padding: 0; box-sizing: border-box; }
  html, body {
    width: 1200px; height: 958px; overflow: hidden;
    background: var(--backdrop);
    font-family: "Lato", Arial, sans-serif;
  }
  .card {
    position: absolute; left: 100px; top: 193px;
    width: 1000px; height: 572px;
    background: var(--card);
    overflow: hidden;
    box-shadow: 0 10px 30px rgba(0,0,0,0.25);
  }
  .card-shapes { position: absolute; inset: 0; }
  .brand {
    position: absolute; top: 120px; width: 260px;
  }
  .brand-orvandel { left: 70px; }
  .brand-brellow { left: 375px; }
  .brand-tamvirk { left: 680px; }
  .brand-heading {
    display: flex; align-items: flex-start; gap: 10px;
  }
  .brand-mark {
    flex: none; width: 14px; height: 14px; margin-top: 7px;
  }
  .brand-orvandel .brand-mark { background: var(--brown); }
  .brand-brellow .brand-mark { background: var(--green); }
  .brand-tamvirk .brand-mark { background: var(--orange); }
  .brand-name {
    font-size: 26px; font-weight: 700; line-height: 1.15; color: var(--ink);
  }
  .brand-web {
    margin-top: 18px; padding-left: 24px;
    font-size: 19px; font-weight: 700; color: var(--ink);
  }
  .contact {
    position: absolute; top: 452px; width: 200px; text-align: center;
    color: var(--light-text); font-size: 19px;
  }
  .contact-orvandel { left: 75px; }
  .contact-brellow { left: 320px; }
  .contact-tamvirk { left: 565px; }
  .contact-icon { display: block; margin: 0 auto 8px; }
  .address {
    position: absolute; left: 330px; top: 531px;
    color: var(--white); font-size: 19px; font-weight: 700;
  }
</style>
</head>
<body>
  <main class="card">
    <svg class="card-shapes" width="1000" height="572" viewBox="0 0 1000 572" aria-hidden="true">
      <path d="M0 420 C250 370 560 380 760 450 C860 485 920 510 960 522 L0 522 Z" fill="var(--charcoal)"/>
      <path d="M80 400 C330 350 640 365 880 505 C640 385 340 382 80 400 Z" fill="var(--green)" stroke="var(--green)" stroke-width="3"/>
      <rect x="0" y="520" width="1000" height="52" fill="var(--green)"/>
    </svg>

    <section class="brand brand-orvandel">
      <div class="brand-heading"><span class="brand-mark"></span><h2 class="brand-name">Orvandel Clinics Australia</h2></div>
      <div class="brand-web">www.orvandel.com</div>
    </section>
    <section class="brand brand-brellow">
      <div class="brand-heading"><span class="brand-mark"></span><h2 class="brand-name">Brellow Clinics Australia</h2></div>
      <div class="brand-web">www.brellow.com</div>
    </section>
    <section class="brand brand-tamvirk">
      <div class="brand-heading"><span class="brand-mark"></span><h2 class="brand-name">Tamvirk Clinics Australia</h2></div>
      <div class="brand-web">www.tamvirk.com</div>
    </section>

    <div class="contact contact-orvandel">
      <svg class="contact-icon" width="18" height="13" viewBox="0 0 18 13" aria-hidden="true"><rect x="0.5" y="0.5" width="17" height="12" fill="var(--green)"/><path d="M1 1 L9 7 L17 1" stroke="var(--charcoal)" fill="none" stroke-width="1.2"/></svg>
      lena@orvandel.com
    </div>
    <div class="contact contact-brellow">
      <svg class="contact-icon" width="18" height="13" viewBox="0 0 18 13" aria-hidden="true"><rect x="0.5" y="0.5" width="17" height="12" fill="var(--green)"/><path d="M1 1 L9 7 L17 1" stroke="var(--charcoal)" fill="none" stroke-width="1.2"/></svg>
      mark@brellow.com
    </div>
    <div class="contact contact-tamvirk">
      <svg class="contact-icon" width="18" height="13" viewBox="0 0 18 13" aria-hidden="true"><rect x="0.5" y="0.5" width="17" height="12" fill="var(--green)"/><path d="M1 1 L9 7 L17 1" stroke="var(--charcoal)" fill="none" stroke-width="1.2"/></svg>
      tess@tamvirk.com
    </div>

    <div class="address">41 Wendle St Parramatta</div>
  </main>
</body>
</html>
```